Epoxy coatings company needs a logo/business card design.

My company name is "Meridian Resin Works", and I am looking for a company logo and business card design.
My initial thought was to use "Æ"in 'Oe'sthetic, and would also like to see ideas on how to play around with the fact that the first 3 letters (Mer) are also the acronym of the company name.
I specialize in garage floor and interior epoxy coatings, paint flake broadcasts, quartz broadcasts, and solid color epoxy floors, concrete repairs.
I like images I've seen of a silhouetted person running a floor grinder. It keeps the design of the card simple. I'm not necessarily opposed to using images of the floors on the card, but I'd prefer to keep the front simple (Company name, my name, phone number, email) and maybe put pictures on the back. I've included a few of my personal pictures of floors I've done (including a before, after, and when the garage was being used after)
My colors are darker green (Fern/Forest/Hunter, etc), and Bronze.

Contact Information for Business Card

Name: Dana Kolvesky Email: meridianresinworks@plinkmail.test Phone: (555)318-2964 Instagram: meridian_resin_works

Colors

Designer to choose colors to be used in the design.

Requirements
Nice to have
• I've included a business card designed for someone else, that contains the silhouette that I'm looking for. The floor grinder that I use is large like the one pictured (Torvex G40R).

```html
<!DOCTYPE html>
<html lang="en">
<head>
<meta charset="utf-8">
<title>Meridian Resin Works – Business Card</title>
<link rel="stylesheet" href="https://fonts.googleapis.com/css2?family=Work+Sans:wght@400;500;700;800&display=swap">
<style>
  :root {
    --forest: #17330f;
    --forest-deep: #122a0c;
    --paper: #ffffff;
    --stage: #d9dadc;
    --ink-light: #f4f6f2;
    --grinder-light: #e4e6e8;
    --grinder-dark: #9a9fa4;
    --before-light: #c9c6c0;
    --before-dark: #8d8a84;
    --after-light: #8f9aa6;
    --after-dark: #3b3f44;
  }
  * { margin: 0; padding: 0; box-sizing: border-box; }
  html, body {
    width: 1200px; height: 800px; overflow: hidden;
    background: var(--stage);
    font-family: "Work Sans", Arial, sans-serif;
  }
  .stage {
    width: 1200px; height: 800px;
    display: flex; flex-direction: column; align-items: center;
    justify-content: center; gap: 60px;
  }
  .card {
    position: relative;
    width: 560px; height: 320px;
    border-radius: 22px;
    overflow: hidden;
    background: var(--forest);
    color: var(--ink-light);
  }
  /* Front */
  .card-front .split { position: absolute; inset: 0; }
  .card-front .machine-photo {
    position: absolute; left: 18px; top: 120px;
    width: 240px; height: 170px;
    border-radius: 40px 30px 20px 50px;
    background: radial-gradient(ellipse at 45% 50%, var(--grinder-light) 0%, var(--grinder-dark) 70%, rgba(154,159,164,0) 100%);
  }
  .contact {
    position: absolute; right: 26px; top: 28px;
    text-align: right;
  }
  .contact .name {
    font-weight: 800; font-size: 23px; letter-spacing: 1px;
    text-transform: uppercase; margin-bottom: 8px;
  }
  .line {
    display: flex; justify-content: flex-end; align-items: center;
    gap: 6px; font-size: 12.5px; line-height: 17px; font-weight: 400;
  }
  .line svg { width: 11px; height: 11px; flex: none; }
  .specialties-title {
    font-weight: 800; font-size: 13px; letter-spacing: .5px;
    text-transform: uppercase; margin: 12px 17px 3px 0;
  }
  .specialties { list-style: none; }
  /* Back */
  .card-back .gallery {
    position: absolute; left: 60px; right: 26px; top: 44px;
    display: flex; gap: 8px;
  }
  .shot { flex: 1; text-align: center; }
  .shot .photo { height: 196px; border-radius: 12px; }
  .shot .photo.before { background: linear-gradient(165deg, var(--before-light), var(--before-dark)); }
  .shot .photo.after { background: linear-gradient(170deg, var(--after-dark) 0%, var(--after-dark) 35%, var(--after-light) 75%, #a9b2bc 100%); }
  .shot .label {
    margin-top: 12px; font-weight: 700; font-size: 15px; letter-spacing: .5px;
  }
</style>
</head>
<body>
<main class="stage">

  <section class="card card-front">
    <svg class="split" viewBox="0 0 560 320" preserveAspectRatio="none" aria-hidden="true">
      <polygon points="0,116 560,116 560,116 0,116" fill="none"/>
      <polygon points="0,112 0,320 320,320 0,112" fill="var(--paper)"/>
      <polygon points="0,112 0,320 320,320 300,320 0,112" fill="var(--paper)"/>
      <polygon points="0,100 205,100 320,320 0,320" fill="var(--paper)"/>
    </svg>
    <div class="machine-photo" role="img" aria-label="Large grey Torvex G40R floor grinder"></div>

    <div class="contact">
      <div class="name">Dana Kolvesky</div>
      <div class="line">(555)318-2964
        <svg viewBox="0 0 12 12"><path d="M3 1.2 4.6 3.6 3.6 4.8a6.5 6.5 0 0 0 3.6 3.6l1.2-1 2.4 1.6-.8 1.8C6 10.6 1.4 6 1.2 2z" fill="currentColor"/></svg>
      </div>
      <div class="line">meridianresinworks@plinkmail.test
        <svg viewBox="0 0 12 12"><rect x="1" y="2.5" width="10" height="7" rx="1" fill="currentColor"/><path d="M1.5 3 6 6.6 10.5 3" stroke="var(--forest)" stroke-width="1" fill="none"/></svg>
      </div>
      <div class="line">meridian_resin_works
        <svg viewBox="0 0 12 12"><circle cx="6" cy="6" r="4.6" stroke="currentColor" stroke-width="1.4" fill="none"/></svg>
      </div>

      <div class="specialties-title">Specializing In</div>
      <ul class="specialties">
        <li class="line">Garage Floor <svg viewBox="0 0 12 12"><circle cx="6" cy="6" r="4.8" stroke="currentColor" stroke-width="1.2" fill="none"/><path d="M3.8 6.1 5.4 7.6 8.3 4.5" stroke="currentColor" stroke-width="1.3" fill="none"/></svg></li>
        <li class="line">Interior Epoxy Coatings <svg viewBox="0 0 12 12"><circle cx="6" cy="6" r="4.8" stroke="currentColor" stroke-width="1.2" fill="none"/><path d="M3.8 6.1 5.4 7.6 8.3 4.5" stroke="currentColor" stroke-width="1.3" fill="none"/></svg></li>
        <li class="line">Paint Flake Broadcasts <svg viewBox="0 0 12 12"><circle cx="6" cy="6" r="4.8" stroke="currentColor" stroke-width="1.2" fill="none"/><path d="M3.8 6.1 5.4 7.6 8.3 4.5" stroke="currentColor" stroke-width="1.3" fill="none"/></svg></li>
        <li class="line">Quartz Broadcasts <svg viewBox="0 0 12 12"><circle cx="6" cy="6" r="4.8" stroke="currentColor" stroke-width="1.2" fill="none"/><path d="M3.8 6.1 5.4 7.6 8.3 4.5" stroke="currentColor" stroke-width="1.3" fill="none"/></svg></li>
        <li class="line">Solid Color Epoxy Floors <svg viewBox="0 0 12 12"><circle cx="6" cy="6" r="4.8" stroke="currentColor" stroke-width="1.2" fill="none"/><path d="M3.8 6.1 5.4 7.6 8.3 4.5" stroke="currentColor" stroke-width="1.3" fill="none"/></svg></li>
        <li class="line">Concrete Repairs. <svg viewBox="0 0 12 12"><circle cx="6" cy="6" r="4.8" stroke="currentColor" stroke-width="1.2" fill="none"/><path d="M3.8 6.1 5.4 7.6 8.3 4.5" stroke="currentColor" stroke-width="1.3" fill="none"/></svg></li>
      </ul>
    </div>
  </section>

  <section class="card card-back">
    <div class="gallery">
      <figure class="shot">
        <div class="photo before" role="img" aria-label="Bare stained concrete garage floor before coating"></div>
        <figcaption class="label">Before</figcaption>
      </figure>
      <figure class="shot">
        <div class="photo after" role="img" aria-label="Garage with finished grey flake epoxy floor and a parked white car"></div>
        <figcaption class="label">After</figcaption>
      </figure>
    </div>
  </section>

</main>
</body>
</html>
```